Marlowe Solutions Business Card

We need a business card design for a software and IT consulting company called marlowe solutions. We would like to feature a kinkajou (it is a small tree-dwelling animal) somewhere in the design. We would like a green color involved somewhere (but not overwhelming). Back of card should be predominately a color, front of the card can be predominately white or predominately a different color than the back.

Information on front of card:

Contact information:
Phone: (555) 214-3907
Email: peter.dunmore@mrlsol.example
Website: www.mrlsol.example

Name: Peter Dunmore
Title: Owner / Developer

Information on back of card:
Marlowe Solutions
Targeted Solutions. Fit to your environment.

Industry/Entity Type

Software

Requirements
Should not have
• Avoid anything that too closely resembles a cartoon or campy feel. This should be professional and modern looking.

```html
<!DOCTYPE html>
<html lang="en">
<head>
<meta charset="utf-8">
<title>Marlowe Solutions Business Card</title>
<link href="https://fonts.googleapis.com/css2?family=Nunito:wght@400;500;800&display=swap" rel="stylesheet">
<style>
  :root {
    --green: #127a3b;
    --tan: #b9a47a;
    --ink: #1d1d1d;
    --white: #ffffff;
    --backdrop: #e9e6e1;
  }
  * { box-sizing: border-box; margin: 0; padding: 0; }
  html, body { width: 1200px; height: 1000px; overflow: hidden; }
  body {
    background: var(--backdrop);
    font-family: "Nunito", sans-serif;
    position: relative;
  }
  .card {
    position: absolute;
    left: 250px;
    width: 700px;
    height: 400px;
    border-radius: 34px;
    overflow: hidden;
    box-shadow: 0 10px 30px rgba(0,0,0,0.18);
  }

  /* Back of card */
  .card-back { top: 60px; background: var(--green); color: var(--white); }
  .back-brand {
    position: absolute; left: 0; right: 0; top: 130px;
    display: flex; align-items: center; justify-content: center; gap: 22px;
  }
  .brand-dot { width: 86px; height: 86px; border-radius: 50%; background: var(--white); flex: none; }
  .back-brand .brand-name {
    font-size: 58px; font-weight: 500; line-height: 1; letter-spacing: 0.5px;
  }
  .tagline {
    position: absolute; right: 46px; bottom: 46px;
    font-size: 26px; font-weight: 400; letter-spacing: 0.3px;
  }

  /* Front of card */
  .card-front { top: 520px; background: var(--white); }
  .front-brand {
    position: absolute; left: 48px; top: 42px;
    color: var(--tan); font-size: 44px; font-weight: 800; line-height: 1;
  }
  .front-mark {
    position: absolute; right: 70px; top: 110px;
    width: 112px; height: 112px; border-radius: 50%; background: var(--tan);
  }
  .person { position: absolute; left: 48px; top: 258px; }
  .person-name { font-size: 36px; font-weight: 800; color: var(--ink); line-height: 1.1; }
  .person-title { font-size: 28px; font-weight: 400; color: var(--tan); line-height: 1.2; }
  .contact {
    position: absolute; right: 48px; top: 272px;
    list-style: none; text-align: right; color: var(--ink);
    font-size: 21px; line-height: 1.45;
  }
  .contact li { display: flex; align-items: center; justify-content: flex-end; gap: 10px; }
  .contact svg { width: 16px; height: 16px; stroke: var(--tan); fill: none; stroke-width: 1.6; }
  .front-band {
    position: absolute; left: 0; right: 0; bottom: 0; height: 52px;
    background: var(--green); color: var(--white);
    display: flex; align-items: center; justify-content: center; gap: 10px;
    font-size: 22px;
  }
  .front-band svg { width: 20px; height: 20px; stroke: var(--white); fill: none; stroke-width: 1.5; }
</style>
</head>
<body>
  <section class="card card-back" aria-label="Back of card">
    <div class="back-brand">
      <span class="brand-dot"></span>
      <span class="brand-name">marlowe solutions</span>
    </div>
    <p class="tagline">Targeted Solutions. Fit to your environment.</p>
  </section>

  <section class="card card-front" aria-label="Front of card">
    <div class="front-brand">marlowe solutions</div>
    <span class="front-mark"></span>
    <div class="person">
      <div class="person-name">Peter Dunmore</div>
      <div class="person-title">Owner / Developer</div>
    </div>
    <ul class="contact">
      <li>(555) 214-3907
        <svg viewBox="0 0 16 16"><rect x="4.5" y="1.5" width="7" height="13" rx="1.5"/><line x1="7" y1="12" x2="9" y2="12"/></svg>
      </li>
      <li>peter.dunmore@mrlsol.example
        <svg viewBox="0 0 16 16"><rect x="1.5" y="3.5" width="13" height="9"/><polyline points="1.5,3.5 8,9 14.5,3.5"/></svg>
      </li>
    </ul>
    <div class="front-band">
      <svg viewBox="0 0 20 20"><circle cx="10" cy="10" r="8"/><ellipse cx="10" cy="10" rx="3.5" ry="8"/><line x1="2" y1="10" x2="18" y2="10"/><line x1="3.5" y1="6" x2="16.5" y2="6"/><line x1="3.5" y1="14" x2="16.5" y2="14"/></svg>
      <span>www.mrlsol.example</span>
    </div>
  </section>
</body>
</html>
```